Bold Plum

I am starting a sharpening service for knives, scissors, and garden tools. It's a sole proprietorship, so it's a small business. The business name is "Bolt Plum." A one or two-page website is fine. Ember Guild has created a logo for me. There should be pictures of the things I sharpen. There will also be a price list for sharpened items. My address is: 18392 Calloway Lane, Stevenson Ranch, CA 91307. Phone number is 661-555-0172

```html
<!DOCTYPE html>
<html lang="en">
<head>
<meta charset="utf-8">
<title>Bolt Plum — Knife &amp; Tool Sharpening in Stevenson Ranch</title>
<link rel="stylesheet" href="https://fonts.googleapis.com/css2?family=Bebas+Neue&family=Inter:wght@400;500;600;700&display=swap">
<style>
:root{
  --bg:#0b0b0b;
  --bg-alt:#141414;
  --panel:#1c1c1c;
  --panel-2:#222;
  --red:#ef3b3b;
  --red-deep:#b51f1f;
  --white:#ffffff;
  --muted:#b9b9b9;
  --dim:#8a8a8a;
  --line:#3a3a3a;
}
*{box-sizing:border-box;margin:0;padding:0}
html,body{width:1200px;height:4921px;overflow:hidden;background:var(--bg);color:var(--white);font-family:"Inter",Arial,sans-serif}
.display{font-family:"Bebas Neue","Arial Narrow",sans-serif;font-weight:400;letter-spacing:.5px;line-height:1}
.accent{color:var(--red)}
section{position:relative;width:1200px;overflow:hidden}

/* brand */
.brand{display:flex;align-items:center;gap:16px;justify-content:center}
.brand-dot{width:26px;height:26px;border-radius:50%;background:var(--red)}
.brand-name{font-family:"Bebas Neue","Arial Narrow",sans-serif;font-size:84px;color:var(--white);line-height:1}

/* buttons */
.btn{display:inline-flex;align-items:center;justify-content:center;gap:12px;font-size:17px;font-weight:600;letter-spacing:1.2px;text-transform:uppercase;color:var(--white);text-decoration:none}
.btn-red{background:var(--red)}
.btn-outline{border:2px solid var(--white)}
.btn svg{width:22px;height:22px}

/* hero */
.hero{height:755px;background:radial-gradient(ellipse at 60% 45%,#3a3a3a 0%,#1b1b1b 35%,#060606 75%)}
.hero-photo{position:absolute;inset:0;background:linear-gradient(150deg,transparent 40%,rgba(140,140,140,.25) 55%,transparent 70%)}
.hero .brand{position:absolute;top:80px;left:0;right:0}
.hero h1{position:absolute;top:275px;left:0;right:0;font-size:70px;text-align:center}
.hero p{position:absolute;top:468px;left:0;right:0;text-align:center;font-size:21px;line-height:32px;color:#d8d8d8}
.hero .actions{position:absolute;top:571px;left:376px;display:flex;gap:18px}
.hero .btn-red{width:214px;height:69px}
.hero .btn-outline{width:214px;height:69px}
.hero-fade{position:absolute;left:0;right:0;bottom:0;height:90px;background:linear-gradient(transparent,#101010)}

/* sharpen carousel */
.sharpen{height:925px;background:#101010;border-top:3px solid transparent;border-image:linear-gradient(90deg,transparent,var(--red-deep),transparent) 1}
.section-title{font-size:64px;text-align:center}
.sharpen .section-title{position:absolute;top:50px;left:0;right:0}
.sharpen .lead{position:absolute;top:142px;left:0;right:0;text-align:center;font-size:21px;line-height:32px;color:var(--muted)}
.card{position:absolute;top:268px;height:570px;background:var(--panel)}
.card-photo{height:442px}
.card-rule{height:4px;background:var(--red);margin:0 65px}
.card h3{font-family:"Bebas Neue","Arial Narrow",sans-serif;font-weight:400;font-size:26px;text-align:center;margin-top:30px}
.card p{font-size:16px;color:var(--muted);text-align:center;margin-top:14px}
.card.side{opacity:.45}
.card.left{left:-511px;width:704px}
.card.main{left:248px;width:704px}
.card.right{left:1011px;width:704px}
.arrow{position:absolute;top:1251px;width:62px;height:62px;border-radius:50%;border:2px solid var(--white);background:rgba(0,0,0,.55);display:flex;align-items:center;justify-content:center}
.arrow svg{width:30px;height:30px}

/* why */
.why{height:632px;background:radial-gradient(ellipse at 40% 55%,#2a2a2a 0%,#121212 45%,#080808 80%)}
.why .section-title{position:absolute;top:110px;left:0;right:0}
.features{position:absolute;top:240px;left:191px;display:grid;grid-template-columns:434px 434px;row-gap:33px}
.feature{display:flex;align-items:center;gap:23px;height:70px}
.feature-icon{width:70px;height:70px;background:var(--red);display:flex;align-items:center;justify-content:center;flex:none}
.feature-icon svg{width:40px;height:40px}
.feature span{font-size:23px;font-weight:500;line-height:32px;text-transform:uppercase}
.divider{position:absolute;left:250px;right:250px;height:3px;background:linear-gradient(90deg,transparent,var(--red-deep),transparent)}

/* pricing */
.pricing{height:765px;background:#0a0a0a}
.pricing .section-title{position:absolute;top:100px;left:0;right:0}
.pricing .lead{position:absolute;top:183px;left:0;right:0;text-align:center;font-size:21px;color:var(--muted)}
.price-card{position:absolute;top:260px;width:432px;background:var(--panel);border-left:5px solid var(--red);border-radius:8px;padding:26px 30px 20px}
.price-card h3{font-family:"Bebas Neue","Arial Narrow",sans-serif;font-weight:400;font-size:29px;margin-bottom:20px}
.price-row{display:flex;align-items:center;height:46px;font-size:17px;color:#cfcfcf}
.price-row .leader{flex:1;border-bottom:1px solid var(--line);margin:0 18px}
.price-row b{font-weight:500;font-size:23px;color:var(--red)}
.pricing .btn-red{position:absolute;top:593px;left:365px;width:447px;height:76px;border-radius:4px;font-size:20px}

/* local */
.local{height:821px;background:radial-gradient(ellipse at 60% 60%,#2c2c2c 0%,#151515 45%,#070707 80%)}
.local h2{position:absolute;top:170px;left:0;right:0;text-align:center;font-size:72px;line-height:68px}
.local .story{position:absolute;top:321px;left:187px;width:826px;height:259px;background:rgba(28,28,28,.92);border-top:4px solid var(--red);border-radius:10px;padding:44px 50px 0;text-align:center;font-size:21px;line-height:37px;color:#d6d6d6}
.dots{position:absolute;top:640px;left:0;right:0;display:flex;justify-content:center;gap:8px}
.dots i{width:11px;height:11px;background:var(--red);transform:rotate(45deg)}

/* contact */
.contact{height:842px;background:#131313}
.contact .section-title{position:absolute;top:60px;left:0;right:0}
.info-card{position:absolute;left:36px;width:535px;background:var(--panel-2);border-left:5px solid var(--red);border-radius:10px;padding:36px 37px}
.info-head{display:flex;align-items:center;gap:20px}
.info-icon{width:56px;height:56px;background:var(--red);border-radius:4px;display:flex;align-items:center;justify-content:center}
.info-icon svg{width:28px;height:28px}
.info-head h3{font-family:"Bebas Neue","Arial Narrow",sans-serif;font-weight:400;font-size:28px}
.phone-big{font-size:42px;font-weight:700;color:var(--red);margin-top:16px;letter-spacing:1px}
.address{font-size:20px;line-height:33px;color:#dcdcdc;margin-top:18px}
.form{position:absolute;top:203px;left:627px;width:535px;height:600px;background:var(--panel);border-radius:10px;padding:36px 36px}
.form label{display:block;font-size:15px;letter-spacing:1px;color:#cfcfcf;margin-bottom:12px}
.form .field{height:54px;background:#0d0d0d;border:1px solid #3c3c3c;margin-bottom:40px}
.form .field.tall{height:165px;margin-bottom:36px}
.form .btn-red{width:100%;height:62px;border-radius:2px;font-size:18px}

/* footer */
.footer{height:181px;background:#0b0b0b;border-top:1px solid #222}
.footer .brand{position:absolute;left:70px;top:55px;justify-content:flex-start}
.footer .brand-name{font-size:66px}
.footer .meta{position:absolute;right:50px;top:50px;text-align:right;font-size:18px;line-height:46px;color:#bdbdbd}
</style>
</head>
<body>

<section class="hero">
  <div class="hero-photo" role="img" aria-label="Close-up photograph of a chef's knife on a dark background"></div>
  <div class="brand"><span class="brand-dot"></span><span class="brand-name">Bolt Plum</span></div>
  <h1 class="display">Professional Knife &amp; Tool<br>Sharpening in Stevenson Ranch</h1>
  <p>Precision sharpening for knives, scissors, and garden tools. Fast<br>turnaround. Local service. Razor-sharp results.</p>
  <div class="actions">
    <a class="btn btn-red" href="#contact"><svg viewBox="0 0 24 24" fill="none" stroke="#fff" stroke-width="1.8"><path d="M5 3h4l2 5-2.5 1.5a11 11 0 0 0 6 6L16 13l5 2v4a2 2 0 0 1-2 2A16 16 0 0 1 3 5a2 2 0 0 1 2-2z"/></svg>Call Now</a>
    <a class="btn btn-outline" href="#pricing">View Pricing</a>
  </div>
  <div class="hero-fade"></div>
</section>

<section class="sharpen">
  <h2 class="section-title display">What We <span class="accent">Sharpen</span></h2>
  <p class="lead">From kitchen knives to garden tools, we restore your edge<br>with precision and care.</p>
  <div class="card side left">
    <div class="card-photo" role="img" aria-label="Photograph of garden tools among dry leaves" style="background:linear-gradient(135deg,#4a3a2a,#2b2118)"></div>
    <div class="card-rule"></div>
    <h3>Garden Tools</h3>
    <p>Professional edge restoration for peak cutting performance.</p>
  </div>
  <div class="card main">
    <div class="card-photo" role="img" aria-label="Photograph of a kitchen knife on a wooden cutting board beside squash" style="background:linear-gradient(100deg,#cfcfcf 0%,#9a9a9a 30%,#7a5a3a 50%,#3b4a30 75%,#c48a20 100%)"></div>
    <div class="card-rule"></div>
    <h3>Kitchen Knives</h3>
    <p>Professional edge restoration for peak cutting performance.</p>
  </div>
  <div class="card side right">
    <div class="card-photo" role="img" aria-label="Photograph of scissors against a brick wall" style="background:linear-gradient(135deg,#7a6a58,#3a2f26)"></div>
    <div class="card-rule"></div>
    <h3>Scissors</h3>
    <p>Professional edge restoration for peak cutting performance.</p>
  </div>
</section>
<div class="arrow" style="left:199px"><svg viewBox="0 0 24 24" fill="none" stroke="#fff" stroke-width="1.6"><path d="M20 12H4M10 6l-6 6 6 6"/></svg></div>
<div class="arrow" style="left:930px"><svg viewBox="0 0 24 24" fill="none" stroke="#fff" stroke-width="1.6"><path d="M4 12h16M14 6l6 6-6 6"/></svg></div>

<section class="why" role="img" aria-label="Faint background photograph of knives">
  <h2 class="section-title display">Why Choose <span class="accent">Bolt Plum</span></h2>
  <div class="features">
    <div class="feature"><div class="feature-icon"><svg viewBox="0 0 24 24" fill="none" stroke="#fff" stroke-width="1.4"><path d="M12 3 4 19h16z M12 3v16 M8 11h8"/></svg></div><span>Precision Sharpening<br>Equipment</span></div>
    <div class="feature"><div class="feature-icon"><svg viewBox="0 0 24 24" fill="none" stroke="#fff" stroke-width="1.4"><circle cx="13" cy="13" r="7"/><path d="M13 9v4l3 2M2 10h4M3 14h3"/></svg></div><span>Fast and Reliable<br>Turnaround</span></div>
    <div class="feature"><div class="feature-icon"><svg viewBox="0 0 24 24" fill="none" stroke="#fff" stroke-width="1.4"><circle cx="12" cy="9" r="5"/><path d="M3 19c3 0 5-2 9-2s6 2 9 2M12 6.5v5"/></svg></div><span>Affordable,<br>Transparent Pricing</span></div>
    <div class="feature"><div class="feature-icon"><svg viewBox="0 0 24 24" fill="none" stroke="#fff" stroke-width="1.4"><path d="M14 4a5 5 0 0 1 5 5c0 4-5 9-5 9s-5-5-5-9a5 5 0 0 1 5-5z"/><circle cx="14" cy="9" r="2"/><path d="M3 20c1-3 3-4 5-4"/></svg></div><span>Locally Owned Small<br>Business</span></div>
    <div class="feature"><div class="feature-icon"><svg viewBox="0 0 24 24" fill="none" stroke="#fff" stroke-width="1.4"><circle cx="12" cy="8" r="5"/><circle cx="8" cy="15" r="5"/><circle cx="16" cy="15" r="5"/></svg></div><span>Custom Design<br>Solutions</span></div>
    <div class="feature"><div class="feature-icon"><svg viewBox="0 0 24 24" fill="none" stroke="#fff" stroke-width="1.4" stroke-dasharray="2 2"><circle cx="12" cy="12" r="8"/><circle cx="12" cy="12" r="3"/></svg></div><span>Tailored to Meet Your<br>Specific Needs</span></div>
  </div>
  <div class="divider" style="bottom:12px"></div>
</section>

<section class="pricing" id="pricing">
  <h2 class="section-title display">Simple &amp; <span class="accent">Transparent</span> Pricing</h2>
  <p class="lead">No hidden fees. Just sharp results.</p>
  <div class="price-card" style="left:151px">
    <h3>Kitchen Knives</h3>
    <div class="price-row"><span>Small (under 6")</span><span class="leader"></span><b>$6</b></div>
    <div class="price-row"><span>Medium (6–8")</span><span class="leader"></span><b>$8</b></div>
    <div class="price-row"><span>Large (8"+)</span><span class="leader"></span><b>$10</b></div>
  </div>
  <div class="price-card" style="left:615px">
    <h3>Other Types</h3>
    <div class="price-row"><span>Scissors</span><span class="leader"></span><b>$7</b></div>
    <div class="price-row"><span>Garden Shears</span><span class="leader"></span><b>$8</b></div>
    <div class="price-row"><span>Pruners &amp; Loppers</span><span class="leader"></span><b>$10</b></div>
    <div class="price-row"><span>Yard Tools</span><span class="leader"></span><b>$12</b></div>
  </div>
  <a class="btn btn-red" href="#contact"><svg viewBox="0 0 24 24" fill="none" stroke="#fff" stroke-width="1.8"><path d="M5 3h4l2 5-2.5 1.5a11 11 0 0 0 6 6L16 13l5 2v4a2 2 0 0 1-2 2A16 16 0 0 1 3 5a2 2 0 0 1 2-2z"/></svg>Call to Schedule Service</a>
  <div class="divider" style="bottom:0"></div>
</section>

<section class="local" role="img" aria-label="Background photograph of a knife on a sharpening stone">
  <h2 class="display">Locally Owned.<br><span class="accent">Professionally Done.</span></h2>
  <div class="story">Bolt Plum is a locally owned sharpening service serving Stevenson Ranch and surrounding communities. As a small business, we take pride in delivering precision work, honest pricing, and personal service. Your tools matter — and we treat them like our own.</div>
  <div class="dots"><i></i><i></i><i></i></div>
  <div class="divider" style="bottom:0"></div>
</section>

<section class="contact" id="contact">
  <h2 class="section-title display">Bolt <span class="accent">Plum</span> Today</h2>
  <div class="info-card" style="top:203px;height:189px">
    <div class="info-head"><div class="info-icon"><svg viewBox="0 0 24 24" fill="none" stroke="#fff" stroke-width="1.8"><path d="M5 3h4l2 5-2.5 1.5a11 11 0 0 0 6 6L16 13l5 2v4a2 2 0 0 1-2 2A16 16 0 0 1 3 5a2 2 0 0 1 2-2z"/></svg></div><h3>Call Us</h3></div>
    <div class="phone-big">661-555-0172</div>
  </div>
  <div class="info-card" style="top:432px;height:209px">
    <div class="info-head"><div class="info-icon"><svg viewBox="0 0 24 24" fill="none" stroke="#fff" stroke-width="1.8"><path d="M12 22s7-7 7-12a7 7 0 0 0-14 0c0 5 7 12 7 12z"/><circle cx="12" cy="10" r="2.5"/></svg></div><h3>Visit Us</h3></div>
    <div class="address">18392 Calloway Lane<br>Stevenson Ranch, CA 91307</div>
  </div>
  <div class="form">
    <label>NAME</label><div class="field"></div>
    <label>PHONE</label><div class="field"></div>
    <label>MESSAGE</label><div class="field tall"></div>
    <div class="btn btn-red"><svg viewBox="0 0 24 24" fill="none" stroke="#fff" stroke-width="1.8"><path d="M22 2 11 13M22 2l-7 20-4-9-9-4z"/></svg>Send Message</div>
  </div>
</section>

<section class="footer">
  <div class="brand"><span class="brand-dot"></span><span class="brand-name">Bolt Plum</span></div>
  <div class="meta">Stevenson Ranch, CA 91307 • 661-555-0172<br>© 2026 Bolt Plum. All rights reserved.</div>
</section>

</body>
</html>
```